Upmarket substance abuse facility needs trifold brochure

New private 16 bed residential substance abuse treatment facility in Mapleton, UT. Facility located in elegant 11,000 home with stunning views of the mountains. Facility is Tudor style with traditional furnishings-an aerial picture of facility is attached.

Attached are the logo, original art drafts, picture of facility and business card. Additional pictures of grounds will be attached later. Professional pictures are being taken on 12-12 and will be uploaded on 12-13 or 14.

The brochure is to emphasis the lovely home and park like grounds that sits at the base of a beautiful mountain range in Mapleton, UT. Focus is on treatment in serene and elegant location. Do not want colors too dark and the style of the maple leaf cannot be changed. Will need space for main picture of house on front, facility description, address and how to contact, treatment philosophy, treatment provided, Admission Criteria, and insurance information.

Do not have the contact information too small or written over a dark color. No solid colored backgrounds.

Overall theme should follow logo and business cards and stay more traditional with use of nature via maple leaf and mountain on logo.
The sample I am using is 8 1/2 tall by 11inches wide. The style is a roll style (folded in thirds). This smaller size can fit in an envelope.

Pages- 3 printed sides in front, 3 in back.

I attached one of the pictures, the picture of the facility from above. The rest of the pictures are being taken on this coming Wed and will be ready on Thursday. I will attach them to the brief then.

We are working on content and hope to have a draft on line later today. The general categories will be:

1. Front page: logo with name- picture of facility from above, descriptor- Residential Substance Dependence Treatment
2. First inside page: List of symptoms and problem behaviors we treat
3.Middle inside page: Intro to facility- first paragraph-what we provide and a second paragraph on treatment philosophy.
4.Third inside page: Services Provided
5. 3rd outside page (fold inside trifold): The Journey Quote
6. Payment options and address and phone at bottom

Note* for some reason the Look and Feel slider keeps reseting to neutral each time. Look at my posting for business cards and logo to see my scales. Also, the color choices offered in the brief are limited. Please use the gold and darker green, not the lighter green shown.
Updates

I just added more information to my brief on trifold style and category headings.

Thank You and I appreciate your hard work on our behalf,

Tessa

I just attached the draft of the text today to go along with the prior posting of he categories. 

I just answered all the questions that came in yesterday regarding text, photos, brochures size and time frames. I also just uploaded a word file with the text for the quote that I forgot to add the first time. 

Good Morning,

Just wanted to provide an update that all the designs are underconsideration by the owner. We will narrow it down once I recieve his feedback later this weekend.  

Thanks for your patience.

Tessa

I just uploaded the professional photographs today. I am still trying to decrease the file size of the arial shot of the facility as it will not upload.

The edited text document was uploaded today.  The items with lines through them should be eliminated.  The items highlighted in yellow are changes and new working.

Thanks.

Target Market(s)

Adults age 18 and over who struggle with substance abuse for alcohol and other substances. Also their families, therapists, medical professionals and insurance companies.

Industry/Entity Type

Residential

Font styles to use
Script
Other font styles liked:
• black chancery for headings

Requirements
Must have
• Same logo
Room for content categories of: treatment provided and philosophy, facility description, admission criteria, insurance/payment and contact information.

Trifold style
Logo and name at the top
Use colors in logo, but they do not have to be used in the same proportions.
Needs to feel comfortable, inviting and gracious.
Nice to have
• more white space and pictures than text space.
Should not have
• Do not use scrolls or other "feminine" embellishments other than the font used in the name/logo.
No solid color backgrounds for entire pages or large sections
Cannot change the maple leaf design
Few if any changes to the mountain depicted if used.

```html
<!DOCTYPE html>
<html lang="en">
<head>
<meta charset="utf-8">
<title>Cedar Hollow Recovery – Trifold Inside Spread</title>
<link href="https://fonts.googleapis.com/css2?family=Carlito:wght@400;700&display=swap" rel="stylesheet">
<style>
  :root {
    --band-green: #3e5a31;
    --rule-green: #3e5a31;
    --ink: #1e1e1e;
    --band-ink: #1f2a18;
    --paper: #ffffff;
    --brand-green: #2f4a25;
    --brand-gold: #b8862b;
    --sky: #8fb0d6;
    --peak: #7c8a94;
    --forest: #3f6a2a;
    --lake: #2b4a7a;
    --meadow: #5a9a2a;
  }
  * { margin: 0; padding: 0; box-sizing: border-box; }
  html, body { width: 1200px; height: 934px; overflow: hidden; background: var(--paper); }
  body { font-family: "Carlito", "Calibri", sans-serif; color: var(--ink); }

  .spread { position: relative; width: 1200px; height: 934px; background: var(--paper); }

  .top-band {
    position: absolute; left: 0; top: 0; width: 1200px; height: 314px;
    background: var(--band-green);
  }
  .band-panel {
    position: absolute; top: 45px; color: var(--band-ink);
    font-size: 15.8px; line-height: 21.5px;
  }
  .band-panel h2 { font-weight: 400; font-size: 15.8px; margin-bottom: 21px; }
  .band-panel.symptoms { left: 41px; width: 330px; }
  .band-panel.philosophy { left: 423px; width: 345px; }

  .brand-box {
    position: absolute; left: 793px; top: 27px; width: 381px; height: 287px;
    background: var(--paper);
    display: flex; align-items: center; justify-content: center; gap: 14px;
  }
  .brand-mark { width: 26px; height: 26px; border-radius: 50%; background: var(--brand-gold); flex: none; }
  .brand-name { font-size: 38px; font-weight: 400; color: var(--brand-green); line-height: 1; }

  .column-rule {
    position: absolute; top: 314px; width: 2px; height: 620px; background: var(--rule-green);
  }
  .column-rule.first { left: 392px; }
  .column-rule.second { left: 791px; }

  .panel { position: absolute; top: 328px; font-size: 15.8px; line-height: 19.6px; }
  .panel.symptom-list { left: 43px; width: 330px; }
  .panel.services { left: 423px; width: 340px; top: 326px; }
  .panel.therapies { left: 817px; width: 340px; top: 326px; }

  .panel h3 { font-size: 19.5px; font-weight: 700; margin-bottom: 20px; }
  .panel p { margin-bottom: 20px; }
  .bullets { list-style: none; }
  .bullets li { padding-left: 0; }
  .bullets li::before { content: "• "; }
  .panel.therapies .bullets { margin-top: 55px; }
  .panel.services .bullets li, .panel.therapies .bullets li { line-height: 21.5px; }

  .photo { position: absolute; top: 666px; height: 240px; }
  .photo.lake-left { left: 43px; width: 322px;
    background: linear-gradient(180deg, var(--sky) 0%, #c9d4de 30%, var(--peak) 45%, var(--forest) 62%, var(--lake) 78%, #1d2f55 100%); }
  .photo.meadow { left: 423px; width: 343px;
    background: linear-gradient(180deg, #3f74c4 0%, #d9e6f5 28%, #4f8a36 50%, var(--meadow) 72%, #7cc03a 100%); }
  .photo.lake-right { left: 817px; width: 324px;
    background: linear-gradient(180deg, var(--sky) 0%, #c9d4de 30%, var(--peak) 45%, var(--forest) 62%, var(--lake) 78%, #1d2f55 100%); }
</style>
</head>
<body>
<main class="spread">
  <section class="top-band">
    <div class="band-panel symptoms">
      <h2>Symptoms Treated:</h2>
      <p>The negative effects of substance dependen-ce can be devastating forfamilies and indi-viduals alike. The impacts of addictions have far reaching&nbsp; consequences on health, self-esteem, finances,legal issues and relationships.If you are struggling with any of the issues listed, we are here to help.</p>
    </div>
    <div class="band-panel philosophy">
      <h2>Philosophy:</h2>
      <p>Personalized 12-step based Jungian practice with integration of a progressive and up to date cognitive behavioral mindfulness practice.&nbsp; To accomplish this, we strive for comprehensive family systems integration of mind, body and spirit into the treatment process. Studies indi-cate family participation significantly improves sustained recovery outcomes.</p>
    </div>
    <div class="brand-box">
      <span class="brand-mark" aria-hidden="true"></span>
      <span class="brand-name">Cedar Hollow Recovery</span>
    </div>
  </section>

  <div class="column-rule first"></div>
  <div class="column-rule second"></div>

  <section class="panel symptom-list">
    <ul class="bullets">
      <li>Legal issues from DUI, possession or violence</li>
      <li>Stealing to pay for your drug of choice</li>
      <li>Significant relationship issues as a result of using</li>
      <li>Inability to keep your financial obligations as a result of addiction</li>
      <li>Poor health related to addiction- poor sleep, weight gain/loss, weakness, nausea, low energy</li>
      <li>Putting your and other peoples lives at risk with high risk behaviors</li>
      <li>Employment and school struggles</li>
      <li>Unable to stop using or limiting drug/addiction use despite attempts to stop</li>
      <li>Low self esteem, anxiety, guilt and depression</li>
      <li>Hiding your addiction and/or the amount used</li>
    </ul>
  </section>

  <section class="panel services">
    <h3>Services Provided:</h3>
    <p>Services include but are not limed to:</p>
    <ul class="bullets">
      <li>Daily group therapy</li>
      <li>Individual therapy twice weekly</li>
      <li>Case Management weekly</li>
      <li>Regular 12-step meetings weekly</li>
      <li>Weekly aftercare follow-up for a year post graduation</li>
      <li>Free aftercare group</li>
      <li>Intensive Outpatient Therapy</li>
    </ul>
  </section>

  <section class="panel therapies">
    <h3>Experiential therapies:</h3>
    <ul class="bullets">
      <li>Equine</li>
      <li>Yoga</li>
      <li>Exercise- on site gym, nature walks, hiking, gardening</li>
      <li>ADA equipped room</li>
      <li>Dietary Consults</li>
      <li>Medical Consults</li>
    </ul>
  </section>

  <div class="photo lake-left" role="img" aria-label="Photo of rocky mountain peaks above a forested alpine lake"></div>
  <div class="photo meadow" role="img" aria-label="Photo of a green hill and meadow under a blue sky with clouds"></div>
  <div class="photo lake-right" role="img" aria-label="Photo of rocky mountain peaks above a forested alpine lake"></div>
</main>
</body>
</html>
```